Bramble Bunnies Business Cards

I need a business card for my new Company called Bramble Bunnies. We create handmade baby moccasins, headbands, t-shirts and more. I want some that will appeal to parents, and to go with the colors of my logo that I have attached. feel free to be creative. I would like my logo placed somewhere on the card.

Industry/Entity Type

Retail

Contact Information for Business Card

Bramble Bunnies
20418 Wexley C #5127
Irvine Ca 92687
Rosalind Hatchett Ceo
Info@Bramble-Bunnies.com
www.Bramble-Bunnies.com
Phone 9495817302

Requirements
Nice to have
• Logo included

```html
<!DOCTYPE html>
<html lang="en">
<head>
<meta charset="utf-8">
<title>Bramble Bunnies – Business Card</title>
<link rel="stylesheet" href="https://fonts.googleapis.com/css2?family=Comic+Neue:wght@400&family=Questrial&display=swap">
<style>
  :root {
    --orange: #ef8457;
    --black: #0b0b0b;
    --white: #ffffff;
    --ink: #141414;
    --backdrop: #6b4a33;
  }
  * { margin: 0; padding: 0; box-sizing: border-box; }
  html, body {
    width: 1200px;
    height: 1000px;
    overflow: hidden;
    background: var(--backdrop);
  }
  .card {
    position: absolute;
    left: 84px;
    top: 191px;
    width: 688px;
    height: 411px;
    background: var(--white);
    transform: scale(1.5);
    transform-origin: 0 0;
    font-family: "Questrial", "Century Gothic", sans-serif;
    color: var(--ink);
    box-shadow: 0 2px 6px rgba(0,0,0,0.35);
  }
  .brand-mark {
    position: absolute;
    left: 130px;
    top: 45px;
    width: 70px;
    height: 70px;
    background: var(--orange);
  }
  .brand-name {
    position: absolute;
    left: 34px;
    top: 152px;
    font-family: "Comic Neue", "Comic Sans MS", cursive;
    font-weight: 400;
    font-size: 41px;
    line-height: 1;
    color: var(--ink);
  }
  .name-band {
    position: absolute;
    left: 0;
    top: 220px;
    width: 688px;
    height: 65px;
    background: linear-gradient(to right, var(--orange) 0 520px, var(--black) 520px);
  }
  .band-mark {
    position: absolute;
    left: 472px;
    top: 12px;
    width: 42px;
    height: 42px;
    background: var(--white);
  }
  .holder {
    position: absolute;
    left: 34px;
    top: 13px;
    color: var(--white);
  }
  .holder-name {
    font-family: "Questrial", "Century Gothic", sans-serif;
    font-weight: 700;
    font-size: 19px;
    line-height: 20px;
  }
  .holder-role {
    font-size: 16px;
    line-height: 18px;
  }
  .contact-list {
    position: absolute;
    left: 34px;
    top: 314px;
    list-style: none;
    font-size: 16.5px;
  }
  .contact-list li {
    display: flex;
    align-items: center;
    height: 22px;
  }
  .contact-list svg {
    width: 12px;
    height: 12px;
    margin-right: 8px;
    fill: var(--orange);
  }
  .address {
    position: absolute;
    left: 461px;
    top: 336px;
    font-style: normal;
    font-size: 16.5px;
    line-height: 22px;
  }
  .base-stripe {
    position: absolute;
    left: 0;
    bottom: 0;
    width: 688px;
    height: 8px;
    background: linear-gradient(to right, var(--orange) 0 493px, var(--black) 493px);
  }
</style>
</head>
<body>
  <article class="card">
    <div class="brand-mark"></div>
    <h1 class="brand-name">Bramble Bunnies</h1>

    <div class="name-band">
      <div class="holder">
        <p class="holder-name">Rosalind Hatchett</p>
        <p class="holder-role">Ceo</p>
      </div>
      <div class="band-mark"></div>
    </div>

    <ul class="contact-list">
      <li>
        <svg viewBox="0 0 12 12" aria-hidden="true"><path d="M2.5 1.2c.5-.4 1.2-.3 1.5.2l1 1.6c.3.5.1 1-.3 1.3l-.6.4c.5 1.4 1.5 2.4 2.9 3l.4-.6c.3-.4.9-.6 1.3-.3l1.6 1c.5.3.6 1 .2 1.5l-.7.8C8.6 11 4 9 1.6 4.8.9 3.5 1 2.5 1.7 1.9z"/></svg>
        9495817302
      </li>
      <li>
        <svg viewBox="0 0 12 12" aria-hidden="true"><path d="M1 2.5h10v7H1z M1.8 3.3 6 6.4l4.2-3.1v-.1H1.8z" fill-rule="evenodd"/></svg>
        info@Bramble-Bunnies.com
      </li>
      <li>
        <svg viewBox="0 0 12 12" aria-hidden="true"><path d="M6 1a5 5 0 1 0 0 10A5 5 0 0 0 6 1zm0 1c.6 0 1.2 1 1.5 2.5h-3C4.8 3 5.4 2 6 2zM2.2 5.3h1.9a8 8 0 0 0 0 1.4H2.2a4 4 0 0 1 0-1.4zm2.7 0h2.2a7 7 0 0 1 0 1.4H4.9a7 7 0 0 1 0-1.4zm3 0h1.9a4 4 0 0 1 0 1.4H7.9a8 8 0 0 0 0-1.4zM4.5 7.5h3C7.2 9 6.6 10 6 10s-1.2-1-1.5-2.5z"/></svg>
        www.bramble-bunnies.com
      </li>
    </ul>

    <address class="address">
      20418 Wexley C #5127<br>
      Irvine Ca 92687
    </address>

    <div class="base-stripe"></div>
  </article>
</body>
</html>
```